Brightwell Commercial Cleaning - Company OverView

I require a 3 page, A4 company folding proschure. I would like to convey a eco frienddly and professional service. Text and images can be found on our company web page www.brightwellcleaning.com.au however we may need some more eco friendly images to convey the right message

The broschure must highlight our companys ISO certification. We are a professional service targeting the corporate industry.

I have hi res images to send and also endorsement and certification logos to send through.

Designer may need to suppl;y some contact and images.

We would like to work with someoe frquently
Updates

HI TEAM, I AM SORRY FOR ANY CONFUSION. I HAVE JUST HAD INSTRUCTIONS THAT THE BROSCHURE WILL NEED TO BE AN A3 SIZE BUT DESIGNED WITH 2 A4 PAGES FRONT AND BACK. SORRY FOR ANY INCONVENIENCE

Target Market(s)

* Corporate
* Professional

Industry/Entity Type

Professional Service

Requirements
Must have
• * Environmental Feel
* Strong Prescense
* Must be CLEAN
* Have 6 A4 pages (Must be a 3 page a4 broschure, Double sided).
Should not have
• * Busy Text
* Old Font

```html
<!DOCTYPE html>
<html lang="en">
<head>
<meta charset="utf-8">
<title>Brightwell Commercial Cleaning – Company Overview</title>
<link rel="stylesheet" href="https://fonts.googleapis.com/css2?family=Roboto+Condensed:wght@300;400&family=Open+Sans:wght@400&display=swap">
<style>
  :root {
    --brand-blue: #2c5ca8;
    --rule-blue: #3f6fb5;
    --tagline-grey: #8a8f96;
    --lime: #b5d334;
    --lime-deep: #8fbf2a;
    --sky-top: #6f9fd3;
    --sky-bottom: #3e79bd;
    --header-top: #e9eaec;
    --header-bottom: #ffffff;
    --leaf-light: #bfe39a;
    --leaf-mid: #6fb43c;
    --leaf-dark: #2f7a1f;
    --white: #ffffff;
  }
  * { margin: 0; padding: 0; box-sizing: border-box; }
  html, body { width: 849px; height: 1200px; overflow: hidden; background: var(--white); }
  .cover {
    position: relative;
    width: 849px;
    height: 1200px;
    overflow: hidden;
    font-family: "Roboto Condensed", "Arial Narrow", sans-serif;
  }
  .masthead {
    position: absolute;
    inset: 0 0 auto 0;
    height: 333px;
    background: linear-gradient(180deg, var(--header-top) 0%, var(--header-bottom) 55%, var(--header-bottom) 100%);
  }
  .brand-name {
    position: absolute;
    left: 128px;
    top: 62px;
    font-weight: 400;
    font-size: 92px;
    line-height: 1;
    color: var(--brand-blue);
    letter-spacing: 1px;
  }
  .brand-rule {
    position: absolute;
    left: 128px;
    top: 206px;
    width: 592px;
    height: 2px;
    background: var(--rule-blue);
  }
  .brand-tagline {
    position: absolute;
    left: 146px;
    top: 218px;
    font-family: "Open Sans", Arial, sans-serif;
    font-size: 27px;
    letter-spacing: 1.5px;
    color: var(--tagline-grey);
  }
  .accent-band {
    position: absolute;
    left: 0;
    width: 849px;
    background: var(--lime);
  }
  .accent-band--top { top: 333px; height: 10px; }
  .accent-band--bottom { top: 795px; height: 14px; background: linear-gradient(90deg, var(--lime-deep), var(--lime)); }
  .hero-image {
    position: absolute;
    left: 0;
    top: 343px;
    width: 849px;
    height: 452px;
    background:
      radial-gradient(ellipse 60% 70% at 85% 35%, var(--leaf-light) 0%, transparent 70%),
      linear-gradient(120deg, var(--leaf-dark) 0%, var(--leaf-mid) 45%, var(--leaf-light) 100%);
  }
  .promise {
    position: absolute;
    left: 0;
    top: 809px;
    width: 849px;
    height: 391px;
    background: linear-gradient(180deg, var(--sky-top) 0%, var(--sky-bottom) 100%);
    text-align: center;
    color: var(--white);
    font-weight: 300;
  }
  .promise-line {
    display: block;
    white-space: nowrap;
    line-height: 1;
  }
  .promise-line--first { margin-top: 96px; }
  .promise-line--second { margin-top: 0px; }
  .promise-small { font-size: 54px; }
  .promise-big { font-size: 94px; color: var(--lime); }
</style>
</head>
<body>
  <main class="cover">
    <header class="masthead">
      <div class="brand-name">Brightwell</div>
      <div class="brand-rule"></div>
      <div class="brand-tagline">Environmental Cleaning Services</div>
    </header>

    <div class="accent-band accent-band--top"></div>
    <div class="hero-image" role="img" aria-label="Close-up photograph of fresh green leaves with water droplets and a ladybird climbing a leaf tip"></div>
    <div class="accent-band accent-band--bottom"></div>

    <section class="promise">
      <span class="promise-line promise-line--first"><span class="promise-small">A </span><span class="promise-big">QUALITY</span><span class="promise-small"> service</span></span>
      <span class="promise-line promise-line--second"><span class="promise-small">that adds </span><span class="promise-big">VALUE</span></span>
    </section>
  </main>
</body>
</html>
```